Web-Design for Electrcian Company

Our Customer is a small business electrian in Switzerland. He is looking for a fresh and innovative website design. He is well known for his extra service, and that they always go for the extra-mile! In his logo you also see that positive and fresh image the try to bring to the customer. the main colors are black, red and white.

the website structure will be:

- home
- services (with submenu for each service)
- references (with submenu for each category of services)
- about us (2 submenus: history and staff)
- links
- Contact

Reason: We are discussing the Proposals with the customer right now

Target Market(s)

Architects, building owners, people from the age of 35 up...

Industry/Entity Type

Small Business

```html
<!DOCTYPE html>
<html lang="en">
<head>
<meta charset="utf-8">
<title>Contact – Brunner + Team Elektro AG</title>
<link rel="stylesheet" href="https://fonts.googleapis.com/css2?family=PT+Sans:wght@400;700&display=swap">
<style>
:root{
  --red:#b90b0b;
  --red-bright:#d0021b;
  --ink:#111111;
  --grey:#7a7a7a;
  --grey-text:#6b6b6b;
  --line:#cfcfcf;
  --field-border:#b5b5b5;
  --footer:#1c1a1a;
  --white:#ffffff;
  --map:#e9e5dc;
  --icon-light:#e6e6e6;
}
*{box-sizing:border-box;margin:0;padding:0}
html,body{width:1200px;height:1165px;overflow:hidden;background:var(--white)}
body{font-family:"PT Sans",Arial,sans-serif;color:var(--ink);position:relative}
.abs{position:absolute}
.utility{left:1078px;top:33px;font-size:13px;color:var(--grey-text)}
.utility span{color:var(--line);margin:0 2px}
.brand-name{left:35px;top:96px;font-size:25px;font-weight:700;color:var(--ink);white-space:nowrap;line-height:34px}
.main-nav a{position:absolute;top:95px;font-size:21px;color:var(--ink);text-decoration:none}
.main-nav .is-active{left:1062px;top:85px;width:105px;height:82px;background:var(--red-bright);color:var(--white);padding:10px 0 0 14px}
.page-band{left:0;top:167px;width:1200px;height:100px;background:var(--red)}
.page-title{left:46px;top:206px;font-size:20px;color:var(--white);font-weight:400}
.doc-icon{border-radius:6px}
.vcard-icon{left:115px;top:315px;width:117px;height:81px;background:linear-gradient(#f2f2f2,#d9d9d9);border-radius:8px}
.pdf-icon{left:296px;top:306px;width:70px;height:90px;background:linear-gradient(#d3322a,#a5120f);border-radius:3px}
.form-title{left:121px;top:428px;font-size:21px;color:var(--grey);font-weight:400;white-space:nowrap}
.field-label{position:absolute;left:121px;font-size:15px;color:var(--grey-text)}
.field{position:absolute;left:121px;width:288px;height:25px;border:1px solid var(--field-border);background:var(--white)}
.field-area{height:55px;resize:none}
.submit{left:120px;top:774px;width:181px;height:28px;border:none;border-radius:4px;background:linear-gradient(#e0212b,#a30d12);color:var(--white);font-family:inherit;font-size:16px}
.divider{left:603px;top:416px;width:1px;height:370px;background:var(--line)}
.map{left:628px;top:436px;width:298px;height:296px;background:var(--map);border:1px solid var(--line)}
.contact-icon{left:966px;top:578px;width:29px;height:29px;background:var(--icon-light);border-radius:5px}
.contact-heading{left:1012px;top:579px;font-size:22px;color:var(--grey);font-weight:400;white-space:nowrap}
.contact-address{left:966px;top:619px;font-size:14px;line-height:16.5px;color:var(--grey-text);font-style:normal}
.site-footer{left:0;top:1093px;width:1200px;height:72px;background:var(--footer)}
.copyright{left:116px;top:1124px;font-size:13px;color:var(--white)}
.footer-nav a{position:absolute;top:1119px;font-size:13px;color:var(--white);text-decoration:none}
</style>
</head>
<body>
<header>
  <div class="abs utility">Help<span>|</span>Support</div>
  <div class="abs brand-name">Brunner + Team Elektro AG</div>
  <nav class="main-nav">
    <a style="left:462px">Home</a>
    <a style="left:571px">Services</a>
    <a style="left:696px">References</a>
    <a style="left:847px">About Us</a>
    <a style="left:982px">links</a>
    <a class="is-active">Contact</a>
  </nav>
</header>

<div class="abs page-band"></div>
<h1 class="abs page-title">CONTACT US</h1>

<div class="abs doc-icon vcard-icon" role="img" aria-label="Business card download icon"></div>
<div class="abs doc-icon pdf-icon" role="img" aria-label="PDF document download icon"></div>

<form>
  <h2 class="abs form-title">Kindly post your valuable Suggestions &amp; &nbsp;Query</h2>
  <label class="field-label" style="top:477px">Enter your Name</label>
  <input class="field" style="top:501px" type="text">
  <label class="field-label" style="top:533px">Enter your Email</label>
  <input class="field" style="top:560px" type="email">
  <label class="field-label" style="top:590px">Enter your Phone Number</label>
  <input class="field" style="top:619px" type="tel">
  <label class="field-label" style="top:646px">Add Your Comments Here:</label>
  <textarea class="field field-area" style="top:668px"></textarea>
  <button class="abs submit" type="button">Submit Query</button>
</form>

<div class="abs divider"></div>

<div class="abs map" role="img" aria-label="Street map showing the office location"></div>

<div class="abs contact-icon">
  <svg width="29" height="29" viewBox="0 0 29 29"><path d="M11 6c-2 1-3 3-3 6 0 4 3 9 7 11 2 1 3 0 4-1l-3-4-2 1c-1-1-2-3-2-5l2-1-3-7z" fill="#bdbdbd"/></svg>
</div>
<h2 class="abs contact-heading">Contact Details</h2>
<address class="abs contact-address">
  Brunner + Team Elektro AG<br>
  Lindenweg 12<br>
  Postfach 210<br>
  9430 Seldorf<br><br>
  Tel 071/555 20 40<br>
  Fax 071/555 20 41
</address>

<footer>
  <div class="abs site-footer"></div>
  <p class="abs copyright">Copyright © 2012 brunnerteamelektro AG . All right reserved</p>
  <nav class="footer-nav">
    <a style="left:686px">Home</a>
    <a style="left:758px">Services</a>
    <a style="left:862px">About Us</a>
    <a style="left:949px">Privacy policy</a>
    <a style="left:1062px">Contact</a>
  </nav>
</footer>
</body>
</html>
```